PowerPoint template for Law Firm

We Need a PowerPoint Template for a Law Firm in Switzerland. We are primarly consult in business law. We Need a template for PowerPoint to Show Information to our Clients (inheritence law, corporate law, legal structures etc.) The design should be contemporary, simple and clear. It should be in harmony with our website: www.tanovik.com Style: professional, structured and clearly arranged. Colors: Blue (R: 1, G: 61: B: 105), white. Font: Calibri Ratio: 16: 9 Esamples attached

Target Market(s)

Business

Font styles to use
Sans Serif

Colors

Designer to choose colors to be used in the design.

Requirements
Must have
• Format 16: 9

```html
<!DOCTYPE html>
<html lang="en">
<head>
<meta charset="utf-8">
<title>Tanovik—Lawyers · Presentation Template</title>
<link href="https://fonts.googleapis.com/css2?family=Carlito:ital,wght@0,400;0,700;1,400&display=swap" rel="stylesheet">
<style>
:root{
  --navy:#013d69;
  --navy-deep:#0d2c54;
  --navy-dark:#002a4a;
  --ink:#1d3557;
  --grey-text:#8a8a8a;
  --grey-mid:#6b6b6b;
  --grey-light:#d9d9d9;
  --grey-pale:#f1f2f4;
  --page:#e4e5e7;
  --white:#ffffff;
}
*{box-sizing:border-box;margin:0;padding:0}
html,body{width:1200px;height:2527px;overflow:hidden;background:var(--page)}
body{font-family:"Carlito",Calibri,Arial,sans-serif;color:var(--ink)}
.deck{display:grid;grid-template-columns:repeat(3,377px);grid-template-rows:repeat(11,212px);gap:16.25px 17.5px;padding:16.25px 17px}
.slide{position:relative;background:var(--white);overflow:hidden;box-shadow:0 1px 3px rgba(0,0,0,.12)}
.abs{position:absolute}
.title{position:absolute;left:0;right:0;top:15px;text-align:center;font-size:15px;color:var(--navy-deep)}
.sub{position:absolute;left:0;right:0;top:35px;text-align:center;font-size:4.5px;color:var(--grey-text)}
.foot{position:absolute;left:10px;bottom:5px;font-size:3.6px;color:var(--navy-deep);font-weight:700}
.pg{position:absolute;right:9px;bottom:5px;font-size:3.6px;color:var(--grey-text)}
.p{font-size:4px;line-height:1.55;color:var(--grey-text)}
.p.j{text-align:justify}
.h{font-size:4.4px;font-weight:700;color:var(--navy-deep)}
.cap{font-size:4.4px;font-weight:700;color:var(--navy)}
.photo{position:absolute}
.num-dot{position:absolute;border-radius:50%;background:var(--navy-deep);color:#fff;font-weight:700;display:flex;align-items:center;justify-content:center}
.btn{position:absolute;border-radius:6px;background:var(--navy-deep);color:#fff;font-size:3.8px;display:flex;align-items:center;justify-content:center;gap:3px}
.btn::before{content:"";width:3px;height:3px;border-radius:50%;background:#fff}
.card{position:absolute;background:#fff;border-radius:8px;box-shadow:0 2px 7px rgba(0,0,0,.13)}
.pill{position:absolute;height:11px;border-radius:6px;background:var(--navy-deep);color:#fff;font-size:4.3px;display:flex;align-items:center;padding-left:5px;gap:4px;white-space:nowrap}
.pill::before{content:"";width:3px;height:3px;border-radius:50%;background:#fff}
.sym{display:none}
svg{display:block}
</style>
</head>
<body>
<svg class="sym" aria-hidden="true">
  <defs>
    <symbol id="hex" viewBox="0 0 30 34"><path d="M15 0 30 8.5V25.5L15 34 0 25.5V8.5Z"/></symbol>
    <symbol id="ic-book" viewBox="0 0 20 20"><path d="M3 4h6c1 0 1 1 1 1v11s0-1-1-1H3ZM17 4h-6c-1 0-1 1-1 1v11s0-1 1-1h6Z" fill="none" stroke="#fff" stroke-width="1.5"/></symbol>
    <symbol id="ic-glass" viewBox="0 0 20 20"><path d="M5 3h10M5 17h10M6 3c0 5 8 5 8 7s-8 2-8 7M14 3c0 5-8 5-8 7s8 2 8 7" fill="none" stroke="#fff" stroke-width="1.5"/></symbol>
    <symbol id="ic-cap" viewBox="0 0 20 20"><path d="M2 8l8-4 8 4-8 4ZM5 10v4c3 2 7 2 10 0v-4" fill="none" stroke="#fff" stroke-width="1.5"/></symbol>
    <symbol id="ic-search" viewBox="0 0 20 20"><circle cx="8.5" cy="8.5" r="5" fill="none" stroke="#fff" stroke-width="1.6"/><path d="M12 12l5 5" stroke="#fff" stroke-width="1.8"/></symbol>
    <symbol id="ic-scale" viewBox="0 0 20 20"><path d="M10 3v14M6 17h8M4 6h12M4 6l-2.5 6h5ZM16 6l-2.5 6h5Z" fill="none" stroke="currentColor" stroke-width="1.3"/></symbol>
    <symbol id="ic-people" viewBox="0 0 20 20"><circle cx="7" cy="7" r="2.5" fill="none" stroke="#fff" stroke-width="1.3"/><circle cx="13" cy="7" r="2.5" fill="none" stroke="#fff" stroke-width="1.3"/><path d="M3 15c0-3 2-4 4-4s4 1 4 4M9 15c0-3 2-4 4-4s4 1 4 4" fill="none" stroke="#fff" stroke-width="1.3"/></symbol>
    <symbol id="ic-target" viewBox="0 0 20 20"><circle cx="10" cy="10" r="6" fill="none" stroke="currentColor" stroke-width="1.3"/><circle cx="10" cy="10" r="2.5" fill="none" stroke="currentColor" stroke-width="1.3"/><path d="M10 10l7-7" stroke="currentColor" stroke-width="1.3"/></symbol>
    <symbol id="ic-link" viewBox="0 0 20 20"><path d="M8 12l4-4M6 10l-2 2a3 3 0 0 0 4 4l2-2M14 10l2-2a3 3 0 0 0-4-4l-2 2" fill="none" stroke="currentColor" stroke-width="1.4"/></symbol>
    <symbol id="ic-mail" viewBox="0 0 20 20"><rect x="3" y="5" width="14" height="10" fill="none" stroke="#fff" stroke-width="1.5"/><path d="M3 5l7 6 7-6" fill="none" stroke="#fff" stroke-width="1.5"/></symbol>
    <symbol id="ic-phone" viewBox="0 0 20 20"><path d="M5 3l3 0 1 4-2 1.5c1 2 2.5 3.5 4.5 4.5L13 11l4 1v3c0 1-1 2-2 2C9 17 3 11 3 5c0-1 1-2 2-2Z" fill="#fff"/></symbol>
    <symbol id="ic-pin" viewBox="0 0 20 20"><path d="M10 2a5.5 5.5 0 0 1 5.5 5.5C15.5 12 10 18 10 18S4.5 12 4.5 7.5A5.5 5.5 0 0 1 10 2Z" fill="#fff"/><circle cx="10" cy="7.5" r="2" fill="#013d69"/></symbol>
    <symbol id="ic-globe" viewBox="0 0 20 20"><circle cx="10" cy="10" r="7" fill="none" stroke="currentColor" stroke-width="1.3"/><ellipse cx="10" cy="10" rx="3" ry="7" fill="none" stroke="currentColor" stroke-width="1.3"/><path d="M3 10h14" stroke="currentColor" stroke-width="1.3"/></symbol>
    <symbol id="ic-check" viewBox="0 0 10 10"><circle cx="5" cy="5" r="4" fill="none" stroke="#cfd6de" stroke-width=".8"/><path d="M3 5l1.5 1.5L7 4" fill="none" stroke="#cfd6de" stroke-width=".8"/></symbol>
    <symbol id="pie" viewBox="-20 -20 40 40"><circle r="19" fill="#0d2c54"/><path d="M0 0L-3.3-18.7A19 19 0 0 1 17.9-6.5Z" fill="#013d69"/><path d="M0 0L17.9-6.5A19 19 0 0 1 14.5 12.2Z" fill="#8a8a8a"/><path d="M0 0L-3.3-18.7A19 19 0 0 0-16.5-9.5Z" fill="#b5b5b5"/></symbol>
  </defs>
</svg>

<main class="deck">

<!-- 1 cover -->
<section class="slide" style="background:var(--navy)">
  <div class="abs" style="left:0;right:0;top:88px;text-align:center;font-size:18px;color:#fff">Tanovik—Lawyers</div>
  <div class="abs" style="left:0;right:0;top:185px;text-align:center;font-size:5.5px;letter-spacing:2.5px;color:#fff">www.tanovik.com</div>
</section>

<!-- 2 title -->
<section class="slide">
  <div class="photo" role="img" aria-label="Soft bright photo of a desk with keyboard and notebook" style="inset:0;background:linear-gradient(135deg,#fbfbfb,#ececee 60%,#f6f6f7)"></div>
  <div class="abs" style="left:143px;top:0;width:93px;height:48px;background:var(--navy);color:#fff;font-size:5.5px;display:flex;align-items:center;justify-content:center">Tanovik—Lawyers</div>
  <div class="abs" style="left:17px;top:108px;width:1.2px;height:80px;background:var(--navy)"></div>
  <div class="abs" style="left:27px;top:112px;font-size:22px;color:var(--navy);letter-spacing:.3px">PRESENATION TITLE</div>
  <div class="abs p" style="left:28px;top:138px">Subtitle of your great here</div>
  <div class="abs" style="left:29px;top:173px;font-size:4.5px;color:var(--navy);line-height:1.5">11.01.2020<br>Lukas Brenner</div>
  <div class="abs" style="left:335px;top:98px;transform:rotate(-90deg);transform-origin:left top;font-size:5px;letter-spacing:1.8px;color:var(--grey-mid);white-space:nowrap;left:366px;top:180px">www.tanovik.com</div>
</section>

<!-- 3 quote -->
<section class="slide">
  <div class="photo" role="img" aria-label="Navy tinted photo of a team meeting" style="inset:0;background:linear-gradient(120deg,#0b3d66,#124a78 50%,#0a3559)"></div>
  <svg class="abs" style="left:120px;top:40px" width="140" height="135" viewBox="0 0 140 135">
    <circle cx="70" cy="67" r="54" fill="none" stroke="#fff" stroke-width="3"/>
    <rect x="6" y="14" width="22" height="22" fill="#104673"/>
    <rect x="112" y="96" width="22" height="22" fill="#104673"/>
    <text x="10" y="35" font-size="24" fill="#fff" font-family="Carlito,sans-serif" font-weight="700">“</text>
    <text x="114" y="117" font-size="24" fill="#fff" font-family="Carlito,sans-serif" font-weight="700">”</text>
  </svg>
  <div class="abs" style="left:145px;top:87px;width:90px;text-align:center;color:#fff;font-style:italic;font-size:7px;line-height:1.3">A clear line fosters solutions – regardless of how straightforward it is.</div>
  <div class="abs" style="left:145px;top:140px;width:90px;text-align:center;color:#fff;font-size:4px">- Tanovik Lawyers -</div>
</section>

<!-- 4 brand -->
<section class="slide">
  <div class="abs" style="left:0;right:0;top:0;height:3px;background:var(--navy)"></div>
  <div class="abs" style="left:0;right:0;bottom:0;height:3px;background:var(--navy)"></div>
  <div class="abs" style="left:0;right:0;top:82px;text-align:center;font-size:33px;font-weight:700;color:var(--navy)">Tanovik—Lawyers</div>
</section>

<!-- 5 agenda -->
<section class="slide">
  <div class="title">Agenda</div><div class="sub">Type the subtitle of your great here</div>
  <div class="abs" style="left:160px;top:72px;width:18px;height:57px;background:var(--navy)"></div>
  <div class="photo" role="img" aria-label="Black and white photo of chess pieces" style="left:34px;top:56px;width:128px;height:146px;background:linear-gradient(160deg,#b9b9b9,#6b6b6b 55%,#2e2e2e)"></div>
  <ol class="abs" style="left:250px;top:57px;list-style:lower-roman;font-size:4.3px;line-height:10px;color:var(--grey-mid)">
    <li>Introduction</li><li>About Us</li><li>Welcome Massage</li><li>Our Law</li><li>Our Problem</li><li>Our Services</li><li>Our Solutions</li><li>Team</li><li>Company profile</li><li>Portfolio</li><li>Company values</li><li>Infographic</li><li>Data Charts</li><li>Connect with Us</li>
  </ol>
  <div class="foot">Tanovik—Lawyers</div><div class="pg">3</div>
</section>

<!-- 6 welcome -->
<section class="slide">
  <div class="abs" style="left:66px;top:46px;font-size:14px;color:var(--navy-deep)">Welcome Message</div>
  <div class="abs p" style="left:66px;top:70px;width:270px">We advise Swiss companies and private clients on business law with clear and practical guidance.</div>
  <div class="abs p j" style="left:66px;top:83px;width:270px">From corporate structures to inheritance planning, we take time to understand each case. Our team explains every option plainly, so that decisions can be made with confidence and with a full view of the risks and the benefits involved for all parties.</div>
  <div class="abs p j" style="left:66px;top:111px;width:270px">We work closely with founders, boards and families. Each mandate is handled with care, precision and discretion, and every client receives a direct contact person throughout.</div>
  <div class="abs p" style="left:66px;top:150px">Best Regards</div>
  <div class="abs" role="img" aria-label="Handwritten signature" style="left:66px;top:158px;width:60px;height:20px;background:linear-gradient(90deg,#eef1f5,#f7f8fa)"></div>
  <div class="foot">Tanovik—Lawyers</div><div class="pg">4</div>
</section>

<!-- 7 about -->
<section class="slide">
  <div class="photo" role="img" aria-label="City skyline at dusk behind a bridge" style="left:226px;top:0;width:151px;height:212px;background:linear-gradient(180deg,#5a5fa8,#9a7fbf 40%,#c79ac2 60%,#3d3654)"></div>
  <div class="abs" style="left:27px;top:52px;font-size:13px;line-height:1.25;color:var(--navy-deep)">About<br>Our Company</div>
  <div class="abs p j" style="left:27px;top:90px;width:128px">We are a Swiss law firm focused on business law. We support companies and families in corporate law, legal structures and inheritance law with precise and reliable advice for every stage of growth and change.</div>
  <div class="abs" style="left:28px;top:150px;width:46px;height:9px;border:.8px solid var(--navy);font-size:3.8px;color:var(--navy);display:flex;align-items:center;justify-content:center">Read more</div>
  <svg class="abs" style="left:82px;top:151px;color:var(--navy)" width="7" height="7"><use href="#ic-globe"/></svg>
  <div class="abs" style="left:92px;top:151px;font-size:4.5px;color:var(--navy-deep)">www.tanovik.com</div>
  <div class="abs" style="left:188px;top:28px;width:88px;height:160px;background:#fff;box-shadow:0 2px 6px rgba(0,0,0,.15)"></div>
  <svg class="abs" style="left:224px;top:46px;color:var(--navy)" width="16" height="16"><use href="#ic-scale"/></svg>
  <div class="abs h" style="left:188px;top:70px;width:88px;text-align:center">Insert title here</div>
  <div class="abs p" style="left:196px;top:77px;width:72px;text-align:center">Short note on this topic for our clients.</div>
  <svg class="abs" style="left:224px;top:112px;color:var(--navy)" width="16" height="16"><use href="#ic-scale"/></svg>
  <div class="abs h" style="left:188px;top:137px;width:88px;text-align:center">Insert title here</div>
  <div class="abs p" style="left:196px;top:144px;width:72px;text-align:center">Short note on this topic for our clients.</div>
  <div class="foot">Tanovik—Lawyers</div>
</section>

<!-- 8 services -->
<section class="slide">
  <div class="title">Our Services</div><div class="sub">Type the subtitle of your great here</div>
  <svg class="abs" style="left:0;top:0" width="377" height="212">
    <g fill="none" stroke="#0d2c54" stroke-width="1.2">
      <circle cx="47" cy="89" r="22"/><circle cx="219" cy="89" r="22"/><circle cx="47" cy="164" r="22"/><circle cx="219" cy="164" r="22"/>
    </g>
    <g font-family="Carlito,sans-serif" font-size="34" fill="#fff" stroke="#0d2c54" stroke-width="1">
      <text x="25" y="102">1</text><text x="197" y="102">2</text><text x="25" y="177">3</text><text x="197" y="177">4</text>
    </g>
  </svg>
  <div class="abs h" style="left:77px;top:72px">Insert title here</div>
  <div class="abs p j" style="left:77px;top:79px;width:100px">Clear advice on business law matters, tailored to the needs of your company and its goals.</div>
  <div class="abs h" style="left:249px;top:72px">Insert title here</div>
  <div class="abs p j" style="left:249px;top:79px;width:100px">Clear advice on business law matters, tailored to the needs of your company and its goals.</div>
  <div class="abs h" style="left:77px;top:146px">Insert title here</div>
  <div class="abs p j" style="left:77px;top:153px;width:100px">Clear advice on business law matters, tailored to the needs of your company and its goals.</div>
  <div class="abs h" style="left:249px;top:146px">Insert title here</div>
  <div class="abs p j" style="left:249px;top:153px;width:100px">Clear advice on business law matters, tailored to the needs of your company and its goals.</div>
  <div class="foot">Tanovik—Lawyers</div><div class="pg">6</div>
</section>

<!-- 9 solutions -->
<section class="slide">
  <div class="title">Our Solutions with Icons</div><div class="sub">Type the subtitle of your great here</div>
  <svg class="abs" style="left:28px;top:73px;fill:var(--navy-deep)" width="30" height="34"><use href="#hex"/></svg>
  <svg class="abs" style="left:36px;top:83px" width="14" height="14"><use href="#ic-book"/></svg>
  <svg class="abs" style="left:206px;top:73px;fill:var(--navy-deep)" width="30" height="34"><use href="#hex"/></svg>
  <svg class="abs" style="left:214px;top:83px" width="14" height="14"><use href="#ic-glass"/></svg>
  <svg class="abs" style="left:28px;top:146px;fill:var(--navy-deep)" width="30" height="34"><use href="#hex"/></svg>
  <svg class="abs" style="left:36px;top:156px" width="14" height="14"><use href="#ic-cap"/></svg>
  <svg class="abs" style="left:206px;top:146px;fill:var(--navy-deep)" width="30" height="34"><use href="#hex"/></svg>
  <svg class="abs" style="left:214px;top:156px" width="14" height="14"><use href="#ic-search"/></svg>
  <div class="abs h" style="left:77px;top:72px">Insert title here</div>
  <div class="abs p j" style="left:77px;top:79px;width:100px">Clear advice on business law matters, tailored to the needs of your company and its goals.</div>
  <div class="abs h" style="left:249px;top:72px">Insert title here</div>
  <div class="abs p j" style="left:249px;top:79px;width:100px">Clear advice on business law matters, tailored to the needs of your company and its goals.</div>
  <div class="abs h" style="left:77px;top:146px">Insert title here</div>
  <div class="abs p j" style="left:77px;top:153px;width:100px">Clear advice on business law matters, tailored to the needs of your company and its goals.</div>
  <div class="abs h" style="left:249px;top:146px">Insert title here</div>
  <div class="abs p j" style="left:249px;top:153px;width:100px">Clear advice on business law matters, tailored to the needs of your company and its goals.</div>
  <div class="foot">Tanovik—Lawyers</div><div class="pg">7</div>
</section>

<!-- 10 timeline -->
<section class="slide">
  <div class="title">Our Timeline</div><div class="sub">Type the subtitle of your great here</div>
  <svg class="abs" style="left:0;top:0" width="377" height="212">
    <g fill="#0d2c54"><circle cx="36" cy="74" r="11"/><circle cx="120" cy="74" r="11"/><circle cx="203" cy="74" r="11"/><circle cx="288" cy="74" r="11"/></g>
    <g fill="none" stroke="#fff" stroke-width="1"><circle cx="36" cy="74" r="4"/><circle cx="120" cy="74" r="4"/><circle cx="203" cy="74" r="4"/><circle cx="288" cy="74" r="4"/></g>
    <g stroke="#d9d9d9" stroke-width=".6"><path d="M47 90v60M131 90v60M214 90v60M299 90v60"/></g>
    <rect x="25" y="158" width="340" height="5" rx="2.5" fill="#e8e8e8"/>
    <rect x="25" y="158" width="143" height="5" rx="2.5" fill="#0d2c54"/>
    <circle cx="36" cy="160.5" r="2" fill="#fff"/><circle cx="120" cy="160.5" r="2" fill="#fff"/>
  </svg>
  <div class="abs" style="left:49px;top:83px;font-size:6px;font-weight:700;color:var(--navy-deep)">2000</div>
  <div class="abs" style="left:133px;top:83px;font-size:6px;font-weight:700;color:var(--navy-deep)">2005</div>
  <div class="abs" style="left:216px;top:83px;font-size:6px;font-weight:700;color:var(--navy-deep)">2016</div>
  <div class="abs" style="left:301px;top:83px;font-size:6px;font-weight:700;color:var(--navy-deep)">2020</div>
  <ul class="abs p" style="left:52px;top:93px;width:62px;padding-left:3px">• Firm founded with a focus on business law.<br>• First clients in corporate law.<br>• Office opened in the city centre.</ul>
  <ul class="abs p" style="left:136px;top:93px;width:62px;padding-left:3px">• Team grew to ten lawyers.<br>• New practice in inheritance law.<br>• Partnerships across the region.</ul>
  <ul class="abs p" style="left:219px;top:93px;width:62px;padding-left:3px">• Second office opened.<br>• Advice on legal structures.<br>• Support for family firms.</ul>
  <ul class="abs p" style="left:304px;top:93px;width:62px;padding-left:3px">• New digital client services.<br>• Focus on startups and boards.<br>• Twenty years of practice.</ul>
  <div class="btn" style="left:31px;top:181px;width:50px;height:12px">Read more</div>
  <div class="btn" style="left:115px;top:181px;width:50px;height:12px">Read more</div>
  <div class="btn" style="left:198px;top:181px;width:50px;height:12px">Read more</div>
  <div class="btn" style="left:283px;top:181px;width:50px;height:12px">Read more</div>
  <div class="foot">Tanovik—Lawyers</div><div class="pg">8</div>
</section>

<!-- 11 heading -->
<section class="slide">
  <div class="photo" role="img" aria-label="Photo of hands pointing at a laptop screen" style="left:20px;top:46px;width:180px;height:110px;background:linear-gradient(120deg,#2f3e4f,#7a8796 50%,#c4ccd4)"></div>
  <div class="num-dot" style="left:215px;top:56px;width:24px;height:24px;font-size:8px;box-shadow:0 0 0 3px #fff,0 0 0 3.6px #d0d6dd">01</div>
  <div class="abs" style="left:247px;top:56px;font-size:13px;color:var(--navy-deep)">Heading Here</div>
  <div class="abs h" style="left:220px;top:96px">Insert subtitle here</div>
  <div class="abs p j" style="left:220px;top:105px;width:122px">We guide businesses through complex legal questions with clear language and well structured steps, from the first meeting to the final agreement and beyond.</div>
  <div class="foot">Tanovik—Lawyers</div><div class="pg">9</div>
</section>

<!-- 12 framed statement -->
<section class="slide">
  <div class="abs" style="left:33px;top:28px;width:312px;height:155px;border:1px solid var(--navy)"></div>
  <div class="abs" style="left:33px;top:50px;width:312px;text-align:center;font-size:14px;color:var(--navy-deep)">Law firm specializing in commercial law</div>
  <div class="abs p" style="left:33px;top:75px;width:312px;text-align:center">Type the subtitle of your great here</div>
  <div class="abs p" style="left:100px;top:96px;width:178px;text-align:center">We support companies in commercial law, contracts and legal structures, and we advise families on inheritance law with care and precision for every case.</div>
  <div class="abs" style="left:33px;top:148px;width:312px;text-align:center;font-size:6px;color:var(--navy-deep)">Tanovik—Lawyers</div>
  <div class="num-dot" style="left:60px;top:170px;width:26px;height:26px;font-size:8px;box-shadow:0 0 0 3px #fff">01</div>
  <div class="foot">Tanovik—Lawyers</div><div class="pg">10</div>
</section>

<!-- 13 projects -->
<section class="slide">
  <div class="abs" style="left:40px;top:93px;font-size:14px;color:var(--navy-deep)">Our Projects</div>
  <div class="abs p" style="left:41px;top:112px">Type the subtitle of your great here</div>
  <div class="num-dot" style="left:160px;top:32px;width:20px;height:20px;font-size:6.5px">01</div>
  <div class="num-dot" style="left:160px;top:73px;width:20px;height:20px;font-size:6.5px">02</div>
  <div class="num-dot" style="left:160px;top:115px;width:20px;height:20px;font-size:6.5px">03</div>
  <div class="num-dot" style="left:160px;top:157px;width:20px;height:20px;font-size:6.5px">04</div>
  <div class="abs h" style="left:192px;top:31px">Insert project title here</div><div class="abs p" style="left:192px;top:38px;width:150px">Restructuring of a family business with new holding and clear roles.</div>
  <div class="abs h" style="left:192px;top:72px">Insert project title here</div><div class="abs p" style="left:192px;top:79px;width:150px">Restructuring of a family business with new holding and clear roles.</div>
  <div class="abs h" style="left:192px;top:114px">Insert project title here</div><div class="abs p" style="left:192px;top:121px;width:150px">Restructuring of a family business with new holding and clear roles.</div>
  <div class="abs h" style="left:192px;top:156px">Insert project title here</div><div class="abs p" style="left:192px;top:163px;width:150px">Restructuring of a family business with new holding and clear roles.</div>
  <div class="foot">Tanovik—Lawyers</div><div class="pg">11</div>
</section>

<!-- 14 section break -->
<section class="slide">
  <div class="abs" style="left:0;right:0;top:92px;text-align:center;font-size:15px;color:var(--navy-deep)">Section Break</div>
  <div class="abs p" style="left:0;right:0;top:113px;text-align:center">Type the subtitle of your great here</div>
  <div class="foot">Tanovik—Lawyers</div><div class="pg">12</div>
</section>

<!-- 15 new connection law -->
<section class="slide">
  <div class="abs" style="left:40px;top:26px;font-size:14px;color:var(--navy-deep)">New Connection Law</div>
  <div class="abs p" style="left:41px;top:45px">Type the subtitle of your great here</div>
  <div class="abs" style="left:26px;top:79px;width:4px;height:4px;border-radius:50%;background:var(--navy-deep)"></div>
  <div class="abs" style="left:26px;top:119px;width:4px;height:4px;border-radius:50%;background:var(--navy-deep)"></div>
  <div class="abs" style="left:26px;top:158px;width:4px;height:4px;border-radius:50%;background:var(--navy-deep)"></div>
  <div class="abs h" style="left:43px;top:78px">New Connection title here</div><div class="abs p" style="left:43px;top:86px;width:145px">A short summary of the new rule and what it means for companies.</div>
  <div class="abs h" style="left:43px;top:118px">New Connection title here</div><div class="abs p" style="left:43px;top:126px;width:145px">A short summary of the new rule and what it means for companies.</div>
  <div class="abs h" style="left:43px;top:157px">New Connection title here</div><div class="abs p" style="left:43px;top:165px;width:145px">A short summary of the new rule and what it means for companies.</div>
  <div class="card" style="left:245px;top:60px;width:90px;height:103px;border-radius:12px"></div>
  <div class="num-dot" style="left:260px;top:81px;width:60px;height:60px;flex-direction:column;font-size:15px;line-height:1">57%<span style="font-size:4px;font-weight:400;margin-top:2px">Percentage value</span></div>
  <div class="foot">Tanovik—Lawyers</div><div class="pg">13</div>
</section>

<!-- 16 bar chart -->
<section class="slide">
  <div class="title">Chart Infographic</div><div class="sub">Type the subtitle of your great here</div>
  <svg class="abs" style="left:0;top:0" width="377" height="212" font-family="Carlito,sans-serif">
    <g stroke="#eee" stroke-width=".4"><path d="M60 50h300M60 70h300M60 90h300M60 110h300M60 130h300M60 150h300M60 170h300"/></g>
    <g font-size="3.5" fill="#999" text-anchor="end"><text x="56" y="51">120</text><text x="56" y="71">100</text><text x="56" y="91">80</text><text x="56" y="111">60</text><text x="56" y="131">40</text><text x="56" y="151">20</text><text x="56" y="171">0</text></g>
    <g fill="#0d2c54">
      <rect x="70" y="70" width="10" height="100"/><rect x="113" y="75" width="10" height="95"/><rect x="156" y="120" width="10" height="50"/><rect x="199" y="70" width="10" height="100"/><rect x="242" y="70" width="10" height="100"/><rect x="285" y="110" width="10" height="60"/><rect x="328" y="120" width="10" height="50"/>
    </g>
    <g fill="#d4d4d4">
      <rect x="81" y="75" width="10" height="95"/><rect x="124" y="85" width="10" height="85"/><rect x="167" y="70" width="10" height="100"/><rect x="210" y="110" width="10" height="60"/><rect x="253" y="75" width="10" height="95"/><rect x="296" y="95" width="10" height="75"/><rect x="339" y="70" width="10" height="100"/>
    </g>
    <g font-size="3.5" fill="#777" text-anchor="middle"><text x="80" y="177">Sun</text><text x="123" y="177">Mon</text><text x="166" y="177">Tu</text><text x="209" y="177">We</text><text x="252" y="177">Th</text><text x="295" y="177">Fr</text><text x="338" y="177">Sa</text></g>
  </svg>
  <div class="foot">Tanovik—Lawyers</div><div class="pg">14</div>
</section>

<!-- 17 pyramid -->
<section class="slide">
  <div class="title">Chart Infographic</div><div class="sub">Type the subtitle of your great here</div>
  <svg class="abs" style="left:0;top:0" width="377" height="212" font-family="Carlito,sans-serif">
    <polygon points="190,40 173.75,61.25 190,71.25" fill="#666"/>
    <polygon points="190,40 190,71.25 208.75,62.5" fill="#444"/>
    <polygon points="173.75,61.25 190,71.25 190,102.5 157.5,82.5" fill="#555"/>
    <polygon points="190,71.25 208.75,62.5 227.5,85 190,102.5" fill="#333"/>
    <polygon points="157.5,82.5 190,102.5 190,133.75 141.25,103.75" fill="#888"/>
    <polygon points="190,102.5 227.5,85 246.25,107.5 190,133.75" fill="#666"/>
    <polygon points="141.25,103.75 190,133.75 190,165 125,125" fill="#013d69"/>
    <polygon points="190,133.75 246.25,107.5 265,130 190,165" fill="#002a4a"/>
    <g fill="#fff" font-size="8" text-anchor="middle">
      <text x="180" y="63" transform="rotate(32 180 63)" font-size="5">04</text>
      <text x="174" y="88" transform="rotate(32 174 88)">03</text>
      <text x="166" y="118" transform="rotate(32 166 118)">02</text>
      <text x="158" y="148" transform="rotate(32 158 148)">01</text>
    </g>
    <g stroke="#999" stroke-width=".4"><path d="M176 56H150M214 64h30M150 110h-20M235 128h35"/></g>
  </svg>
  <div class="abs h" style="left:82px;top:62px;width:70px;text-align:center">Insert title here</div><div class="abs p" style="left:82px;top:69px;width:70px;text-align:center">Short note on this step.</div>
  <div class="abs h" style="left:255px;top:52px;width:70px">Insert title here</div><div class="abs p" style="left:255px;top:59px;width:70px">Short note on this step.</div>
  <div class="abs h" style="left:58px;top:127px;width:70px;text-align:center">Insert title here</div><div class="abs p" style="left:58px;top:134px;width:70px;text-align:center">Short note on this step.</div>
  <div class="abs h" style="left:288px;top:122px;width:70px">Insert title here</div><div class="abs p" style="left:288px;top:129px;width:70px">Short note on this step.</div>
  <div class="foot">Tanovik—Lawyers</div><div class="pg">15</div>
</section>

<!-- 18 three factors -->
<section class="slide">
  <div class="title">Three Factors</div><div class="sub">Type the subtitle of your great here</div>
  <div class="card" style="left:30px;top:70px;width:90px;height:110px"></div>
  <div class="card" style="left:143px;top:70px;width:90px;height:110px"></div>
  <div class="card" style="left:256px;top:70px;width:90px;height:110px"></div>
  <svg class="abs" style="left:64px;top:55px;fill:var(--navy-deep)" width="22" height="25"><use href="#hex"/></svg>
  <svg class="abs" style="left:69px;top:61px" width="12" height="12"><use href="#ic-people"/></svg>
  <svg class="abs" style="left:177px;top:55px;fill:var(--navy-deep)" width="22" height="25"><use href="#hex"/></svg>
  <svg class="abs" style="left:182px;top:61px" width="12" height="12"><use href="#ic-people"/></svg>
  <svg class="abs" style="left:290px;top:55px;fill:var(--navy-deep)" width="22" height="25"><use href="#hex"/></svg>
  <svg class="abs" style="left:295px;top:61px" width="12" height="12"><use href="#ic-people"/></svg>
  <div class="abs h" style="left:30px;top:89px;width:90px;text-align:center">Insert factor title here</div><div class="abs p" style="left:42px;top:104px;width:66px;text-align:center;line-height:2">Clear steps, honest advice and fair fees for each client.</div>
  <div class="abs h" style="left:143px;top:89px;width:90px;text-align:center">Insert factor title here</div><div class="abs p" style="left:155px;top:104px;width:66px;text-align:center;line-height:2">Clear steps, honest advice and fair fees for each client.</div>
  <div class="abs h" style="left:256px;top:89px;width:90px;text-align:center">Insert factor title here</div><div class="abs p" style="left:268px;top:104px;width:66px;text-align:center;line-height:2">Clear steps, honest advice and fair fees for each client.</div>
  <div class="foot">Tanovik—Lawyers</div><div class="pg">16</div>
</section>

<!-- 19 pie chart -->
<section class="slide">
  <div class="title">Pie Chart</div><div class="sub">Type the subtitle of your great here</div>
  <svg class="abs" style="left:0;top:0" width="377" height="212" font-family="Carlito,sans-serif">
    <polygon points="150,122 165,104 200,104 200,170 165,170" fill="#e6e6e6"/>
    <g transform="translate(90 130)">
      <circle r="46" fill="#0d2c54"/>
      <path d="M0 0L-8-45.3A46 46 0 0 1 43.2-15.7Z" fill="#013d69"/>
      <path d="M0 0L43.2-15.7A46 46 0 0 1 35.2 29.6Z" fill="#6b6b6b"/>
    </g>
    <rect x="170" y="104" width="32" height="27" fill="#9a9a9a"/><rect x="170" y="141" width="32" height="27" fill="#9a9a9a"/>
    <g fill="#fff" font-size="8" text-anchor="middle"><text x="186" y="121">74%</text><text x="186" y="158">18%</text></g>
    <g font-size="3.5" fill="#666"><circle cx="87" cy="191" r="1.2" fill="#0d2c54"/><text x="90" y="192.3">1st Qtr</text><circle cx="106" cy="191" r="1.2" fill="#013d69"/><text x="109" y="192.3">2nd Qtr</text><circle cx="126" cy="191" r="1.2" fill="#6b6b6b"/><text x="129" y="192.3">3rd Qtr</text><circle cx="146" cy="191" r="1.2" fill="#bbb"/><text x="149" y="192.3">4th Qtr</text></g>
  </svg>
  <div class="abs" style="left:95px;top:64px;font-size:6px;font-weight:700;color:var(--navy-deep)">Your Text here</div>
  <div class="abs h" style="left:232px;top:72px">Insert title here</div><div class="abs p" style="left:232px;top:79px;width:108px">Short summary of the figures shown in this chart for clients.</div>
  <div class="abs h" style="left:232px;top:111px">Insert title here</div><div class="abs p" style="left:232px;top:118px;width:108px">Short summary of the figures shown in this chart for clients.</div>
  <div class="abs h" style="left:232px;top:150px">Insert title here</div><div class="abs p" style="left:232px;top:157px;width:108px">Short summary of the figures shown in this chart for clients.</div>
  <div class="foot">Tanovik—Lawyers</div><div class="pg">17</div>
</section>

<!-- 20 table -->
<section class="slide">
  <div class="title">Table chart</div><div class="sub">Type the subtitle of your great here</div>
  <svg class="abs" style="left:0;top:0" width="377" height="212" font-family="Carlito,sans-serif">
    <rect x="46" y="63" width="285" height="10" fill="#0d2c54"/>
    <g stroke="#fff" stroke-width="1"><path d="M110 63v10M150 63v10M195 63v10M245 63v10"/></g>
    <g fill="#fff" font-size="4.8" text-anchor="middle"><text x="78" y="70">Title here</text><text x="130" y="70">Law</text><text x="172" y="70">Value</text><text x="220" y="70">Brand</text><text x="288" y="70">Quality</text></g>
    <g fill="#f0f0f0"><rect x="46" y="75" width="285" height="10"/><rect x="46" y="99" width="285" height="10"/><rect x="46" y="123" width="285" height="10"/><rect x="46" y="147" width="285" height="10"/></g>
    <g fill="#999" font-size="4.3" text-anchor="middle">
      <text x="78" y="81.5">Example one</text><text x="130" y="81.5">3</text><text x="172" y="81.5">10</text><text x="220" y="81.5">New</text><text x="288" y="81.5">15%</text>
      <text x="78" y="93.5">Example two</text><text x="130" y="93.5">6</text><text x="172" y="93.5">45</text><text x="220" y="93.5">New</text><text x="288" y="93.5">60%</text>
      <text x="78" y="105.5">Example three</text><text x="130" y="105.5">6</text><text x="172" y="105.5">67</text><text x="220" y="105.5">New</text><text x="288" y="105.5">67%</text>
      <text x="78" y="117.5">Example four</text><text x="130" y="117.5">9</text><text x="172" y="117.5">94</text><text x="220" y="117.5">New</text><text x="288" y="117.5">22%</text>
      <text x="78" y="129.5">Example five</text><text x="130" y="129.5">2</text><text x="172" y="129.5">50</text><text x="220" y="129.5">New</text><text x="288" y="129.5">15%</text>
      <text x="78" y="141.5">Example six</text><text x="130" y="141.5">1</text><text x="172" y="141.5">90</text><text x="220" y="141.5">New</text><text x="288" y="141.5">09%</text>
      <text x="78" y="153.5">Example seven</text><text x="130" y="153.5">5</text><text x="172" y="153.5">31</text><text x="220" y="153.5">New</text><text x="288" y="153.5">10%</text>
    </g>
  </svg>
  <div class="abs p" style="left:36px;top:170px;width:305px;text-align:center">This table compares sample values across areas of law. Replace each row with your own figures to show clients a clear overview of the data.</div>
  <div class="foot">Tanovik—Lawyers</div><div class="pg">18</div>
</section>

<!-- 21 one column -->
<section class="slide">
  <div class="title">One Column Text</div><div class="sub">Type the subtitle of your great here</div>
  <div class="abs p j" style="left:56px;top:62px;width:275px;line-height:1.9">Our firm advises companies and private clients across Switzerland on business law. We handle corporate law, contracts, legal structures and inheritance law, always with a clear plan and plain words. Every mandate starts with listening, so that we understand the goals, the risks and the people involved before we suggest a way forward.</div>
  <div class="abs p j" style="left:56px;top:122px;width:275px;line-height:1.9">We keep our clients informed at each step and explain every option in a simple way. This allows owners, boards and families to decide with confidence. Our team combines long experience with modern tools, and we stay close to our clients long after a case is closed, as a trusted partner for future questions.</div>
  <div class="foot">Tanovik—Lawyers</div><div class="pg">19</div>
</section>

<!-- 22 two column -->
<section class="slide">
  <div class="title">Two Column Text</div><div class="sub">Type the subtitle of your great here</div>
  <div class="abs p j" style="left:52px;top:68px;width:126px;line-height:1.95">Our firm advises companies and private clients on business law. We handle corporate law, contracts, legal structures and inheritance law with a clear plan and plain words. Every mandate starts with listening, so we understand the goals and risks before we suggest a path. We keep clients informed at each step.</div>
  <div class="abs p j" style="left:205px;top:68px;width:126px;line-height:1.95">We explain every option in a simple way so that owners, boards and families can decide with confidence. Our team combines long experience with modern tools, and we remain close to clients long after a case is closed, as a trusted partner for new questions in the years ahead.</div>
  <div class="foot">Tanovik—Lawyers</div><div class="pg">20</div>
</section>

<!-- 23 bullets -->
<section class="slide">
  <div class="title">Bullet Point Text</div><div class="sub">Type the subtitle of your great here</div>
  <div class="abs" style="left:50px;top:70px;width:4px;height:4px;border-radius:50%;background:var(--navy-deep)"></div>
  <div class="abs" style="left:50px;top:101px;width:4px;height:4px;border-radius:50%;background:var(--navy-deep)"></div>
  <div class="abs" style="left:50px;top:132px;width:4px;height:4px;border-radius:50%;background:var(--navy-deep)"></div>
  <div class="abs" style="left:50px;top:163px;width:4px;height:4px;border-radius:50%;background:var(--navy-deep)"></div>
  <div class="abs h" style="left:61px;top:68px">Your new title here</div><div class="abs p" style="left:61px;top:75px;width:270px">A brief point that explains one key topic for clients, such as corporate law or legal structures, in a few clear words.</div>
  <div class="abs h" style="left:61px;top:99px">Your new title here</div><div class="abs p" style="left:61px;top:106px;width:270px">A brief point that explains one key topic for clients, such as corporate law or legal structures, in a few clear words.</div>
  <div class="abs h" style="left:61px;top:130px">Your new title here</div><div class="abs p" style="left:61px;top:137px;width:270px">A brief point that explains one key topic for clients, such as corporate law or legal structures, in a few clear words.</div>
  <div class="abs h" style="left:61px;top:161px">Your new title here</div><div class="abs p" style="left:61px;top:168px;width:270px">A brief point that explains one key topic for clients, such as corporate law or legal structures, in a few clear words.</div>
  <div class="foot">Tanovik—Lawyers</div><div class="pg">21</div>
</section>

<!-- 24 creative heading -->
<section class="slide">
  <div class="abs" style="left:16px;top:20px;font-size:14px;color:var(--navy-deep)">Creative Heading</div>
  <div class="abs p" style="left:17px;top:39px">Type the subtitle of your great here</div>
  <div class="abs" style="left:32px;top:65px;width:86px;height:86px;border-radius:50%;background:var(--navy-deep)"></div>
  <div class="abs" style="left:145px;top:65px;width:86px;height:86px;border-radius:50%;border:1px solid var(--navy-deep)"></div>
  <div class="abs" style="left:259px;top:65px;width:86px;height:86px;border-radius:50%;border:1px solid var(--navy-deep)"></div>
  <svg class="abs" style="left:67px;top:100px;color:#fff" width="16" height="16"><use href="#ic-scale"/></svg>
  <svg class="abs" style="left:180px;top:100px;color:var(--navy-deep)" width="16" height="16"><use href="#ic-target"/></svg>
  <svg class="abs" style="left:294px;top:100px;color:var(--navy-deep)" width="16" height="16"><use href="#ic-link"/></svg>
  <div class="abs cap" style="left:32px;top:158px;width:86px;text-align:center">Creative title here</div><div class="abs p" style="left:45px;top:165px;width:60px;text-align:center">Short note on this area of law.</div>
  <div class="abs cap" style="left:145px;top:158px;width:86px;text-align:center">Creative title here</div><div class="abs p" style="left:158px;top:165px;width:60px;text-align:center">Short note on this area of law.</div>
  <div class="abs cap" style="left:259px;top:158px;width:86px;text-align:center">Creative title here</div><div class="abs p" style="left:272px;top:165px;width:60px;text-align:center">Short note on this area of law.</div>
  <div class="foot">Tanovik—Lawyers</div><div class="pg">22</div>
</section>

<!-- 25 picture with text -->
<section class="slide">
  <div class="photo" role="img" aria-label="Top view photo of hands typing on a laptop beside a coffee cup" style="left:0;top:0;width:160px;height:212px;background:linear-gradient(150deg,#f3f3f3,#bfc2c6 45%,#6e7378 70%,#e9e9e9)"></div>
  <div class="abs" style="left:128px;top:10px;width:249px;height:202px;background:#fff"></div>
  <div class="abs" style="left:120px;top:205px;width:40px;height:7px;background:var(--navy-deep)"></div>
  <div class="abs" style="left:128px;top:16px;width:249px;text-align:center;font-size:14px;color:var(--navy-deep)">Picture with Text</div>
  <div class="abs p" style="left:128px;top:35px;width:249px;text-align:center">Type the subtitle of your great here</div>
  <div class="abs p j" style="left:162px;top:85px;width:188px;line-height:1.95">We support companies and families with clear advice on business law. From founding a company to planning a succession, our team explains each step plainly and stays close to every client, so that important decisions can be made with full confidence and a clear view.</div>
  <div class="abs" style="left:182px;top:203px;font-size:3.6px;color:var(--navy-deep);font-weight:700">Tanovik—Lawyers</div><div class="pg">23</div>
</section>

<!-- 26 price table -->
<section class="slide">
  <div class="title">Price Table</div><div class="sub">Type the subtitle of your great here</div>
  <div class="card" style="left:58px;top:48px;width:86px;height:152px;border-radius:4px"></div>
  <div class="card" style="left:150px;top:48px;width:86px;height:152px;border-radius:4px"></div>
  <div class="card" style="left:242px;top:48px;width:86px;height:152px;border-radius:4px"></div>
  <div class="abs" style="left:58px;top:52px;width:86px;text-align:center;font-size:5px;font-weight:700;color:#2b8fd6">BASIC</div>
  <div class="abs" style="left:150px;top:52px;width:86px;text-align:center;font-size:5px;font-weight:700;color:var(--navy)">STANDED</div>
  <div class="abs" style="left:242px;top:52px;width:86px;text-align:center;font-size:5px;font-weight:700;color:var(--navy-deep)">PREMIUM</div>
  <svg class="abs" style="left:0;top:0" width="377" height="212">
    <circle cx="101" cy="72" r="8" fill="#2b8fd6"/><circle cx="101" cy="72" r="4" fill="none" stroke="#fff"/>
    <circle cx="193" cy="72" r="8" fill="#1d5fa8"/><path d="M193 67l1.5 3.3 3.5.3-2.7 2.3.9 3.5-3.2-1.9-3.2 1.9.9-3.5-2.7-2.3 3.5-.3Z" fill="#fff"/>
    <circle cx="285" cy="72" r="8" fill="#0d2c54"/><path d="M281 70h8l-4 5Z" fill="none" stroke="#fff" stroke-width=".8"/>
    <g><use href="#ic-check" x="66" y="90" width="5" height="5"/><use href="#ic-check" x="66" y="101" width="5" height="5"/><use href="#ic-check" x="66" y="112" width="5" height="5"/><use href="#ic-check" x="66" y="123" width="5" height="5"/>
    <use href="#ic-check" x="158" y="90" width="5" height="5"/><use href="#ic-check" x="158" y="101" width="5" height="5"/><use href="#ic-check" x="158" y="112" width="5" height="5"/><use href="#ic-check" x="158" y="123" width="5" height="5"/>
    <use href="#ic-check" x="250" y="90" width="5" height="5"/><use href="#ic-check" x="250" y="101" width="5" height="5"/><use href="#ic-check" x="250" y="112" width="5" height="5"/><use href="#ic-check" x="250" y="123" width="5" height="5"/></g>
    <g fill="#e3e3e3"><rect x="75" y="91" width="50" height="1.2"/><rect x="75" y="94" width="40" height="1.2"/><rect x="75" y="102" width="50" height="1.2"/><rect x="75" y="105" width="40" height="1.2"/><rect x="75" y="113" width="50" height="1.2"/><rect x="75" y="116" width="40" height="1.2"/><rect x="75" y="124" width="50" height="1.2"/><rect x="75" y="127" width="40" height="1.2"/>
    <rect x="167" y="91" width="50" height="1.2"/><rect x="167" y="94" width="40" height="1.2"/><rect x="167" y="102" width="50" height="1.2"/><rect x="167" y="105" width="40" height="1.2"/><rect x="167" y="113" width="50" height="1.2"/><rect x="167" y="116" width="40" height="1.2"/><rect x="167" y="124" width="50" height="1.2"/><rect x="167" y="127" width="40" height="1.2"/>
    <rect x="259" y="91" width="50" height="1.2"/><rect x="259" y="94" width="40" height="1.2"/><rect x="259" y="102" width="50" height="1.2"/><rect x="259" y="105" width="40" height="1.2"/><rect x="259" y="113" width="50" height="1.2"/><rect x="259" y="116" width="40" height="1.2"/><rect x="259" y="124" width="50" height="1.2"/><rect x="259" y="127" width="40" height="1.2"/></g>
  </svg>
  <div class="abs" style="left:58px;top:155px;width:86px;text-align:center;font-size:15px;font-weight:700;color:#2b8fd6">$30<sup style="font-size:6px">99</sup></div>
  <div class="abs" style="left:150px;top:155px;width:86px;text-align:center;font-size:15px;font-weight:700;color:#1d5fa8">$60<sup style="font-size:6px">99</sup></div>
  <div class="abs" style="left:242px;top:155px;width:86px;text-align:center;font-size:15px;font-weight:700;color:var(--navy-deep)">$150<sup style="font-size:6px">99</sup></div>
  <div class="btn" style="left:80px;top:179px;width:42px;height:9px;background:#2b8fd6">BUY NOW</div>
  <div class="btn" style="left:172px;top:179px;width:42px;height:9px;background:#1d5fa8">BUY NOW</div>
  <div class="btn" style="left:264px;top:179px;width:42px;height:9px">BUY NOW</div>
  <div class="foot">Tanovik—Lawyers</div><div class="pg">24</div>
</section>

<!-- 27 case study -->
<section class="slide">
  <div class="abs" style="left:24px;top:36px;font-size:14px;color:var(--navy-deep)">Client Case Study</div>
  <div class="abs p" style="left:25px;top:56px">Type the subtitle of your great here</div>
  <div class="abs p j" style="left:26px;top:90px;width:196px;line-height:1.9">A family business asked us to plan its succession and set up a new holding. We reviewed the current structure, spoke with every owner and drafted a clear plan. The result was a smooth transfer, lower risk and a structure ready for growth over the coming years.</div>
  <div class="photo" role="img" aria-label="Photo of people at a conference hall in purple light" style="left:238px;top:28px;width:127px;height:70px;background:linear-gradient(135deg,#2a2450,#6a3b8a 50%,#1c1b3a)"></div>
  <div class="abs" style="left:238px;top:98px;width:127px;height:78px;background:var(--navy-deep)"></div>
  <div class="abs" style="left:244px;top:108px;width:1px;height:50px;background:#fff"></div>
  <div class="abs" style="left:250px;top:113px;width:108px;font-size:4px;line-height:1.45;color:#fff">A clear plan for a family business, with a new holding, fair roles for each owner and a smooth transfer to the next generation.</div>
  <div class="foot">Tanovik—Lawyers</div><div class="pg">25</div>
</section>

<!-- 28 team -->
<section class="slide">
  <div class="title">Our Team</div><div class="sub">Type the subtitle of your great here</div>
  <div class="card" style="left:25px;top:56px;width:72px;height:138px;border-radius:3px"></div>
  <div class="card" style="left:111px;top:56px;width:72px;height:138px;border-radius:3px"></div>
  <div class="card" style="left:197px;top:56px;width:72px;height:138px;border-radius:3px"></div>
  <div class="card" style="left:283px;top:56px;width:72px;height:138px;border-radius:3px"></div>
  <div class="photo" role="img" aria-label="Portrait photo of a team member" style="left:44px;top:64px;width:34px;height:34px;border-radius:50%;background:linear-gradient(#9a9a9a,#4a4a4a)"></div>
  <div class="photo" role="img" aria-label="Portrait photo of a team member" style="left:130px;top:64px;width:34px;height:34px;border-radius:50%;background:linear-gradient(#8a8a8a,#3a3a3a)"></div>
  <div class="photo" role="img" aria-label="Portrait photo of a team member" style="left:216px;top:64px;width:34px;height:34px;border-radius:50%;background:linear-gradient(#a3a3a3,#505050)"></div>
  <div class="photo" role="img" aria-label="Portrait photo of a team member" style="left:302px;top:64px;width:34px;height:34px;border-radius:50%;background:linear-gradient(#e6e6e6,#9c9c9c)"></div>
  <div class="abs h" style="left:25px;top:108px;width:72px;text-align:center">Example Name<br><span style="font-weight:400;color:var(--grey-mid)">Text</span></div>
  <div class="abs h" style="left:111px;top:108px;width:72px;text-align:center">Example Name<br><span style="font-weight:400;color:var(--grey-mid)">Text</span></div>
  <div class="abs h" style="left:197px;top:108px;width:72px;text-align:center">Example Name<br><span style="font-weight:400;color:var(--grey-mid)">Text</span></div>
  <div class="abs h" style="left:283px;top:108px;width:72px;text-align:center">Example Name<br><span style="font-weight:400;color:var(--grey-mid)">Text</span></div>
  <div class="abs p" style="left:30px;top:128px;width:62px;text-align:center">Lawyer for corporate law with many years of practice.</div>
  <div class="abs p" style="left:116px;top:128px;width:62px;text-align:center">Lawyer for corporate law with many years of practice.</div>
  <div class="abs p" style="left:202px;top:128px;width:62px;text-align:center">Lawyer for corporate law with many years of practice.</div>
  <div class="abs p" style="left:288px;top:128px;width:62px;text-align:center">Lawyer for corporate law with many years of practice.</div>
  <svg class="abs" style="left:0;top:0" width="377" height="212"><g fill="none" stroke="#9fb0c4" stroke-width=".5">
    <circle cx="53" cy="176" r="2.5"/><circle cx="61" cy="176" r="2.5"/><circle cx="69" cy="176" r="2.5"/>
    <circle cx="139" cy="176" r="2.5"/><circle cx="147" cy="176" r="2.5"/><circle cx="155" cy="176" r="2.5"/>
    <circle cx="225" cy="176" r="2.5"/><circle cx="233" cy="176" r="2.5"/><circle cx="241" cy="176" r="2.5"/>
    <circle cx="311" cy="176" r="2.5"/><circle cx="319" cy="176" r="2.5"/><circle cx="327" cy="176" r="2.5"/></g></svg>
  <div class="foot">Tanovik—Lawyers</div><div class="pg">26</div>
</section>

<!-- 29 structure -->
<section class="slide">
  <div class="title">Our Structure</div><div class="sub">Type the subtitle of your great here</div>
  <svg class="abs" style="left:0;top:0" width="377" height="212">
    <g fill="none" stroke="#999" stroke-width=".6">
      <path d="M193 62v77M95 112h200M95 112v6M295 112v6M120 143h150M120 143v6M270 143v6"/>
    </g>
  </svg>
  <div class="pill" style="left:157px;top:45px;width:70px">Chair Person</div>
  <div class="pill" style="left:160px;top:68px;width:64px">Deputy Chair</div>
  <div class="pill" style="left:160px;top:93px;width:66px">Secretary</div>
  <div class="pill" style="left:160px;top:120px;width:66px">Admin</div>
  <div class="pill" style="left:60px;top:106px;width:66px">Mining Manager</div>
  <div class="pill" style="left:262px;top:106px;width:70px">Logistic Manager</div>
  <div class="pill" style="left:86px;top:143px;width:64px">Field Manager</div>
  <div class="pill" style="left:235px;top:143px;width:72px">Marketing Manager</div>
  <div class="foot">Tanovik—Lawyers</div><div class="pg">27</div>
</section>

<!-- 30 mockup -->
<section class="slide">
  <div class="abs" style="left:24px;top:44px;font-size:14px;line-height:1.2;color:var(--navy-deep)">Mockup<br>with text/chart</div>
  <div class="abs p" style="left:25px;top:80px">Type the subtitle of your great here</div>
  <div class="abs p j" style="left:26px;top:108px;width:110px;line-height:1.95">Show your own slides or web pages on this screen to give clients a clear view of your work and results.</div>
  <div class="photo" role="img" aria-label="Desktop monitor showing a dashboard with charts" style="left:163px;top:36px;width:190px;height:160px;background:linear-gradient(180deg,#2b2b2b 0,#2b2b2b 75%,#8d8d8d 75%,#cfcfcf 100%);border-radius:3px"></div>
  <div class="abs" style="left:170px;top:42px;width:176px;height:108px;background:linear-gradient(160deg,#f5f7fa,#dfe5ec)"></div>
  <div class="foot">Tanovik—Lawyers</div><div class="pg">28</div>
</section>

<!-- 31 more charts -->
<section class="slide">
  <div class="title">More Charts</div><div class="sub">Type the subtitle of your great here</div>
  <svg class="abs" style="left:0;top:0" width="377" height="212" font-family="Carlito,sans-serif">
    <g>
      <use href="#pie" x="38" y="63" width="40" height="40"/><use href="#pie" x="117" y="63" width="40" height="40"/><use href="#pie" x="196" y="63" width="40" height="40"/><use href="#pie" x="275" y="63" width="40" height="40"/>
      <use href="#pie" x="38" y="128" width="40" height="40"/><use href="#pie" x="117" y="128" width="40" height="40"/><use href="#pie" x="196" y="128" width="40" height="40"/><use href="#pie" x="275" y="128" width="40" height="40"/>
    </g>
    <g font-size="3.4" fill="#666" id="legend">
      <g transform="translate(82 71)"><circle r="1" fill="#0d2c54"/><text x="2" y="1.2">1st Qtr</text><circle cy="6" r="1" fill="#013d69"/><text x="2" y="7.2">2nd Qtr</text><circle cy="12" r="1" fill="#8a8a8a"/><text x="2" y="13.2">3rd Qtr</text><circle cy="18" r="1" fill="#b5b5b5"/><text x="2" y="19.2">4th Qtr</text></g>
      <g transform="translate(161 71)"><circle r="1" fill="#0d2c54"/><text x="2" y="1.2">1st Qtr</text><circle cy="6" r="1" fill="#013d69"/><text x="2" y="7.2">2nd Qtr</text><circle cy="12" r="1" fill="#8a8a8a"/><text x="2" y="13.2">3rd Qtr</text><circle cy="18" r="1" fill="#b5b5b5"/><text x="2" y="19.2">4th Qtr</text></g>
      <g transform="translate(240 71)"><circle r="1" fill="#0d2c54"/><text x="2" y="1.2">1st Qtr</text><circle cy="6" r="1" fill="#013d69"/><text x="2" y="7.2">2nd Qtr</text><circle cy="12" r="1" fill="#8a8a8a"/><text x="2" y="13.2">3rd Qtr</text><circle cy="18" r="1" fill="#b5b5b5"/><text x="2" y="19.2">4th Qtr</text></g>
      <g transform="translate(319 71)"><circle r="1" fill="#0d2c54"/><text x="2" y="1.2">1st Qtr</text><circle cy="6" r="1" fill="#013d69"/><text x="2" y="7.2">2nd Qtr</text><circle cy="12" r="1" fill="#8a8a8a"/><text x="2" y="13.2">3rd Qtr</text><circle cy="18" r="1" fill="#b5b5b5"/><text x="2" y="19.2">4th Qtr</text></g>
      <g transform="translate(82 136)"><circle r="1" fill="#0d2c54"/><text x="2" y="1.2">1st Qtr</text><circle cy="6" r="1" fill="#013d69"/><text x="2" y="7.2">2nd Qtr</text><circle cy="12" r="1" fill="#8a8a8a"/><text x="2" y="13.2">3rd Qtr</text><circle cy="18" r="1" fill="#b5b5b5"/><text x="2" y="19.2">4th Qtr</text></g>
      <g transform="translate(161 136)"><circle r="1" fill="#0d2c54"/><text x="2" y="1.2">1st Qtr</text><circle cy="6" r="1" fill="#013d69"/><text x="2" y="7.2">2nd Qtr</text><circle cy="12" r="1" fill="#8a8a8a"/><text x="2" y="13.2">3rd Qtr</text><circle cy="18" r="1" fill="#b5b5b5"/><text x="2" y="19.2">4th Qtr</text></g>
      <g transform="translate(240 136)"><circle r="1" fill="#0d2c54"/><text x="2" y="1.2">1st Qtr</text><circle cy="6" r="1" fill="#013d69"/><text x="2" y="7.2">2nd Qtr</text><circle cy="12" r="1" fill="#8a8a8a"/><text x="2" y="13.2">3rd Qtr</text><circle cy="18" r="1" fill="#b5b5b5"/><text x="2" y="19.2">4th Qtr</text></g>
      <g transform="translate(319 136)"><circle r="1" fill="#0d2c54"/><text x="2" y="1.2">1st Qtr</text><circle cy="6" r="1" fill="#013d69"/><text x="2" y="7.2">2nd Qtr</text><circle cy="12" r="1" fill="#8a8a8a"/><text x="2" y="13.2">3rd Qtr</text><circle cy="18" r="1" fill="#b5b5b5"/><text x="2" y="19.2">4th Qtr</text></g>
    </g>
  </svg>
  <div class="foot">Tanovik—Lawyers</div><div class="pg">29</div>
</section>

<!-- 32 get in touch -->
<section class="slide">
  <div class="title">Get In Touch</div><div class="sub">Type the subtitle of your great here</div>
  <div class="abs p" style="left:110px;top:50px;width:157px;text-align:center">We look forward to hearing from you. Contact us for a first talk about your case.</div>
  <div class="abs" style="left:0;right:0;top:66px;text-align:center;font-size:25px;color:#dfe3ea">Tanovik—Lawyers</div>
  <svg class="abs" style="left:38px;top:114px;fill:var(--navy-deep)" width="26" height="30"><use href="#hex"/></svg>
  <svg class="abs" style="left:44px;top:122px" width="14" height="14"><use href="#ic-mail"/></svg>
  <svg class="abs" style="left:131px;top:114px;fill:var(--navy-deep)" width="26" height="30"><use href="#hex"/></svg>
  <svg class="abs" style="left:137px;top:122px" width="14" height="14"><use href="#ic-phone"/></svg>
  <svg class="abs" style="left:224px;top:114px;fill:var(--navy-deep)" width="26" height="30"><use href="#hex"/></svg>
  <svg class="abs" style="left:230px;top:122px" width="14" height="14"><use href="#ic-pin"/></svg>
  <svg class="abs" style="left:317px;top:114px;fill:var(--navy-deep)" width="26" height="30"><use href="#hex"/></svg>
  <svg class="abs" style="left:323px;top:122px;color:#fff" width="14" height="14"><use href="#ic-globe"/></svg>
  <div class="abs p" style="left:11px;top:152px;width:80px;text-align:center">contact@tanovik.com</div>
  <div class="abs p" style="left:104px;top:152px;width:80px;text-align:center">+41 71 555 01 00</div>
  <div class="abs p" style="left:192px;top:152px;width:90px;text-align:center;line-height:1.3">Tanovik Lawyers AG<br>Seestrasse 4 – CH-9000 Musterdorf</div>
  <div class="abs p" style="left:290px;top:152px;width:80px;text-align:center">www.tanovik.com</div>
  <div class="foot">Tanovik—Lawyers</div><div class="pg">30</div>
</section>

<!-- 33 thank you -->
<section class="slide">
  <div class="photo" role="img" aria-label="Soft bright photo of a desk with keyboard and notebook" style="inset:0;background:linear-gradient(135deg,#f9f9fa,#e9eaec 55%,#f4f4f5)"></div>
  <div class="abs" style="left:0;right:0;top:90px;text-align:center;font-size:24px;color:var(--navy-deep)">Thank You</div>
  <div class="abs" style="left:0;right:0;top:121px;text-align:center;font-size:3.8px;font-weight:700;color:var(--navy-deep)">Tanovik—Lawyers</div>
</section>

</main>
</body>
</html>
```